Radiant Crossing - An Exciting Mission & Book Cover Project

Help me to inspire people to live their best life! This is a mission, not just a design project.
I need a Book Cover designed to keep me inspired on the process of writing my book.
Book Title: Radiant Crossing
Tag Line: Three Simple Steps to get out of your own way, SuperCharge your Life and Step into Purpose!
Author: Marlis Quenby

The three steps are: Ownership, Vision and Action (Not sure if this should be on the front or back of the book cover)

The book is a self-help, motivational book. Personal development.
The cover needs to be strong and capture peoples attention, especially with competing shelf space. I almost see a fire ball of flame or explosion that will grab peoples attention.
My company is The Lantern Institute. I have added the company logo and a few pages of my presentation and topic outline to give an idea.
Maybe: The Lantern Institute logo on back of the cover. website is marlisquenby.com

THOUGHT: People should be able to take a photo of them holding the book cover showing what area of life they want Radiant Crossing in. This is why the front cover must be so visual and powerful that they want to take a photo with it. Ie. Explosion, fire, strong and bold.

Target Market(s)

Anyone who feels stuck and needs to breakthrough and move forward in life.

Industry/Entity Type

Motivation

Font styles to use
Serif
Sans Serif

Colors
ec1f27
f37122
fbed22

Requirements
Must have
• The design must be STRONG, SIMPLE, STAND OUT ON BOOK SHELVES.
Must have an open file to swap the photo and copy out.

Back Cover Page
1) Summary
2) 2-3 testimonials. One sentence.
3) About the Author (maybe with photo)
4) Lantern Institute logo
5) Website: radiantcrossing.com and marlisquenby.com
Nice to have
• If my photo works somewhere that would be great. I will change the photo later.
Added Where's Your Harbor? a nice cover example.
Should not have
• Right now I am writing the summary for the back of the cover. For now use Loreum Ipsum text and 2-3 recommendations. Again, I will get these only later.

```html
<!DOCTYPE html>
<html lang="en">
<head>
<meta charset="utf-8">
<title>Radiant Crossing – Book Cover</title>
<link rel="stylesheet" href="https://fonts.googleapis.com/css2?family=Roboto:wght@400;500;700;900&family=Hind:wght@600;700&display=swap">
<style>
:root{
  --yellow:#fbed22;
  --black:#0b0b0b;
  --white:#ffffff;
  --grey:#d9d9d9;
  --stage:#e9e6e1;
}
*{box-sizing:border-box;margin:0;padding:0}
html,body{width:1200px;height:1165px;overflow:hidden;background:var(--stage)}
body{font-family:"Roboto",sans-serif;position:relative}

.wrap{position:absolute;left:10px;top:62px;width:1180px;height:1040px;display:flex;box-shadow:0 10px 30px rgba(0,0,0,.25)}

/* Back cover */
.back{width:555px;height:100%;background:var(--black);color:var(--white);position:relative;padding:38px 34px 0 40px;overflow:hidden}
.back-title{font-family:"Hind",sans-serif;font-weight:700;color:var(--yellow);font-size:54px;line-height:1;letter-spacing:-.5px}
.back-sub{font-size:10px;letter-spacing:.3px;border-top:2px solid var(--white);margin-top:6px;padding-top:5px;text-transform:uppercase}
.summary{font-size:11.5px;line-height:1.3;text-align:justify;margin-top:24px;color:var(--grey)}
.rule{height:3px;background:var(--white)}
.rule.top{margin-top:26px}
.course-title{font-family:"Hind",sans-serif;font-weight:700;color:var(--yellow);font-size:50px;text-align:center;line-height:1;padding:16px 0 8px}
.keys{display:flex;justify-content:space-between;margin-top:30px;gap:8px}
.key{flex:1;text-align:center}
.key-num{font-size:17px;font-weight:500;text-transform:uppercase}
.key-name{font-family:"Hind",sans-serif;font-weight:700;color:var(--yellow);font-size:30px;line-height:1;margin-bottom:14px}
.key ul{list-style:none}
.key li{margin-bottom:9px}
.key li b{display:block;font-size:7.5px;font-weight:700;text-transform:uppercase}
.key li span{display:block;font-size:6.2px;text-transform:uppercase;color:var(--grey)}
.rule.bottom{margin-top:18px}
.author-photo{position:absolute;left:0;bottom:0;width:215px;height:320px;background:linear-gradient(180deg,#8a8a8a,#3a3a3a 70%,#1a1a1a)}
.author-block{position:absolute;left:230px;top:725px;right:30px}
.author-name{font-family:"Hind",sans-serif;font-weight:700;color:var(--yellow);font-size:34px;line-height:1}
.bio{font-size:11px;line-height:1.35;text-align:justify;margin-top:10px;color:var(--grey)}
.urls{color:var(--yellow);font-size:11.5px;margin-top:14px;line-height:1.35}
.institute{display:flex;align-items:center;gap:8px;margin-top:12px;font-size:13px;font-weight:500;text-transform:uppercase;letter-spacing:.5px}
.institute i{width:14px;height:14px;border-radius:50%;background:var(--yellow);display:block}

/* Spine */
.spine{width:70px;height:100%;background:var(--yellow);position:relative;border-left:1px solid #c9bd10;border-right:1px solid #c9bd10}
.spine-text{position:absolute;left:50%;top:40px;transform-origin:0 0;transform:rotate(90deg) translateY(-50%);white-space:nowrap;font-weight:900;font-size:34px;color:var(--black)}
.spine-band{position:absolute;left:0;right:0;bottom:0;height:34px;background:var(--black)}

/* Front cover */
.front{width:555px;height:100%;background:var(--yellow);position:relative;overflow:hidden}
.front-author{position:absolute;left:80px;top:38px;font-weight:900;font-size:40px;color:var(--black);letter-spacing:-.5px}
.title-box{position:absolute;background:var(--black);color:var(--yellow);font-weight:900;line-height:1}
.title-main{left:80px;top:108px;width:450px;height:148px;font-size:104px;padding:18px 0 0 20px;letter-spacing:-2px}
.title-second{left:80px;top:276px;padding:14px 18px 14px 14px;font-size:56px}
.bomb-art{position:absolute;left:40px;top:505px;width:540px;height:540px;border-radius:50%;background:var(--black)}
.tagline{position:absolute;left:110px;width:390px;top:555px;text-align:center;font-family:"Hind",sans-serif;font-weight:700;font-size:44px;line-height:50px;color:var(--yellow)}
.tagline .hi{color:var(--white)}
.front-band{position:absolute;left:0;right:0;bottom:0;height:34px;background:var(--black)}
</style>
</head>
<body>
<div class="wrap">

  <section class="back">
    <h2 class="back-title">Radiant Crossing</h2>
    <p class="back-sub">Three simple steps to get out of your own way, supercharge your life and step into purpose</p>
    <p class="summary">Lorem ipsum dolor sit amet, consectetur adipisicing elit, sed do eiusmod tempor incididunt ut labore et dolore magna aliqua. Ut enim ad minim veniam, quis nostrud exercitation ullamco laboris nisi ut aliquip ex ea commodo consequat. Duis aute irure dolor in reprehenderit in voluptate velit esse cillum dolore eu fugiat nulla pariatur. Excepteur sint occaecat cupidatat non proident, sunt in culpa qui officia deserunt mollit anim id est laborum. Sed ut perspiciatis unde omnis iste natus error sit voluptatem accusantium doloremque laudantium, totam rem aperiam, eaque ipsa quae ab illo inventore veritatis et quasi arc.</p>

    <div class="rule top"></div>
    <h3 class="course-title">Course Content</h3>
    <div class="rule"></div>

    <div class="keys">
      <div class="key">
        <p class="key-num">First Key</p>
        <p class="key-name">OWNERSHIP</p>
        <ul>
          <li><b>Embracing your journey</b><span>100% ownership + radical acceptance</span></li>
          <li><b>The perfect experience you needed to have</b><span>in order to wake up</span></li>
          <li><b>Growth through pain &amp; challenge</b><span>finding purpose in pain</span></li>
          <li><b>Letting go of toxic emotions</b><span>anger, resentment, guilt, shame, jealousy</span></li>
          <li><b>Shifting from victim to victor</b><span>choosing healthy emotions</span></li>
          <li><b>Reframing your story</b><span>shaping an empowered narrative</span></li>
          <li><b>Breaking up with the idea of perfection</b><span>because it doesn't exist</span></li>
        </ul>
      </div>
      <div class="key">
        <p class="key-num">Second Key</p>
        <p class="key-name">VISION</p>
        <ul>
          <li><b>The power of vision</b><span>the secret jet fuel of action</span></li>
          <li><b>Being authentic to yourself</b><span>it's your life, not anyone else's</span></li>
          <li><b>Crafting your 10-year goal</b><span>starting with the end in mind</span></li>
          <li><b>Chunking down</b><span>short + medium term goals</span></li>
          <li><b>Future pacing</b><span>experience your nirvana right now</span></li>
          <li><b>How your goal serves others</b><span>our ultimate purpose</span></li>
          <li><b>Constant realignment</b><span>tweaking our goals as we go</span></li>
        </ul>
      </div>
      <div class="key">
        <p class="key-num">Third Key</p>
        <p class="key-name">ACTION</p>
        <ul>
          <li><b>Blocks to taking action</b><span>fear, procrastination &amp; people pleasing</span></li>
          <li><b>Small steps daily</b><span>the power of consistency &amp; persistence</span></li>
          <li><b>Comfort vs. calling</b><span>doing things you don't want to</span></li>
          <li><b>Showing up with excellence</b><span>habits of peak performers</span></li>
          <li><b>VIP support structure</b><span>mentors &amp; building a team</span></li>
          <li><b>Grit &amp; resilience</b><span>dealing with 'no'</span></li>
          <li><b>Constant daily growth</b><span>growth through what you go through</span></li>
        </ul>
      </div>
    </div>
    <div class="rule bottom"></div>

    <div class="author-photo" role="img" aria-label="Black and white portrait photo of the author in a dark suit"></div>
    <div class="author-block">
      <h3 class="author-name">Marlis Quenby</h3>
      <p class="bio">Lorem ipsum dolor sit amet, consectetur adipisicing elit, sed do eiusmod tempor incididunt ut labore et dolore magna aliqua. Ut enim ad minim veniam, quis nostrud exercitation ullamco laboris nisi ut aliquip ex ea commodo consequat. Duis aute irure dolor in reprehenderit in voluptate velit esse cillum dolore eu fugiat nulla pariatur. Excepteur sint occaecat cupidatat non proident, sunt in culpa qui officia deserunt mollit anim id est laborum. Sed ut perspiciatis unde omnis iste natus error sit voluptatem accusantium doloremque laudantium.</p>
      <p class="urls">radiantcrossing.com<br>and marlisquenby.com</p>
      <p class="institute"><i></i>The Lantern Institute</p>
    </div>
  </section>

  <section class="spine">
    <p class="spine-text">Radiant Crossing &nbsp;|&nbsp; Marlis Quenby</p>
    <div class="spine-band"></div>
  </section>

  <section class="front">
    <p class="front-author">MARLIS QUENBY</p>
    <div class="title-box title-main">Radiant</div>
    <div class="title-box title-second">Crossing</div>

    <div class="bomb-art" role="img" aria-label="Illustration of a large black bomb with a lit, sparking fuse and a trail of footprints"></div>

    <p class="tagline">Three<br>Simple Steps<br>to get out of your<br>own way,<br><span class="hi">SuperCharge<br>your Life</span><br>and Step into<br>Purpose!</p>
    <div class="front-band"></div>
  </section>

</div>
</body>
</html>
```